依頼概要
■依頼の目的/概要
弊社ではあささんぽ、あさひを浴びようと思えるSNSアプリの制作を行っております。
ほしぞらノートアプリでは毎日の記録をつけるためのライフログ系の機能を制作しております。

ライフログとして自分の記録を見返したり、他のユーザーからも見てもらえる機能がある日記のデザイン及びその画面のUI制作をお願いします。

■依頼の詳細
ユーザーが投稿するのは朝日を含めた毎朝の日記で自分のほしぞらノート(本のテイスト)の左ページを投稿します(アプリ上ホーム画面)。その日記投稿や朝散歩をすればするほど幸せの証として「きらりリボン」を報酬として獲得し、毎朝獲得したハートを自分のほしぞらノートの右ページに貯めておけます(アプリ上ほしぞらノート画面)。

今回トライアルでお願いしたいのはユーザーが朝日を投稿するホーム画面のUIです(左ページ)。
必要な要項といたしましては、
・ユーザーが撮影した朝日の写真(必須)
・日付(必須)
・天気※
・場所※
・気温※
・日記コメント※
・自分のキャラクター(こちらは素材があります)※

を入れられるようにしたいと考えております。
※は、ユーザー任意で入れたり、非表示にできます

スワイプすると、他のユーザーの日記のページをめくるような感覚のモーションの検討もしています。

こちらをトライアルという形で、採用された方には別画面/別バージョンの本のデザインや詳細なUIなどご相談したいと考えております。追加のUIのお見積りなども含め、ご提案いただけますと幸いです。

現在の開発中の仮デザインを添付しますが、よりよいデザインを是非、応募いただけますと幸いです。

画面UIのデザインがイメージと合っていた為。

この度、ご提案いただきありがとうございました。ご厚情にお応えすることができず、誠に申し訳ございません。勝手ではございますが、これに懲りず今後ともお付き合いくださいますようお願い申し上げます。

```html
<!DOCTYPE html>
<html lang="ja">
<head>
<meta charset="utf-8">
<title>HOSHIZORA Note</title>
<link href="https://fonts.googleapis.com/css2?family=Playfair+Display:wght@700&family=Josefin+Sans:wght@400;600&family=Zen+Kaku+Gothic+New:wght@400;500&display=swap" rel="stylesheet">
<style>
  :root {
    --paper: #fcf8f3;
    --ink: #2d3a66;
    --text: #2a2a2a;
    --icon-green: #2f6b4f;
    --nav-bg: #ffffff;
    --nav-icon: #6b6b6b;
    --binding: #bdbdbd;
  }
  * { margin: 0; padding: 0; box-sizing: border-box; }
  html, body { width: 1200px; height: 2596px; overflow: hidden; background: var(--paper); }
  .screen {
    position: relative; width: 1200px; height: 2596px;
    background: var(--paper);
    border-radius: 0 0 64px 64px; overflow: hidden;
    font-family: "Zen Kaku Gothic New", sans-serif; color: var(--text);
  }
  .binding {
    position: absolute; left: 0; top: 0; width: 170px; height: 2392px;
    background: linear-gradient(90deg, #cfcfcf 0%, var(--binding) 100%);
  }
  .page { position: absolute; left: 240px; top: 0; width: 780px; }
  .diary-title {
    position: absolute; top: 56px; left: 72px;
    font-family: "Playfair Display", serif; font-weight: 700;
    font-size: 70px; letter-spacing: 4px; color: var(--ink); white-space: nowrap;
  }
  .diary-date {
    position: absolute; top: 196px; left: 52px;
    font-family: "Josefin Sans", sans-serif; font-weight: 600;
    font-size: 58px; letter-spacing: 4px; color: var(--ink); white-space: nowrap;
  }
  .diary-date small { font-family: "Zen Kaku Gothic New", sans-serif; font-size: 40px; font-weight: 500; letter-spacing: 0; }
  .diary-date .weekday { font-size: 36px; font-weight: 400; margin-left: 10px; }
  .sunrise-photo {
    position: absolute; top: 348px; left: 0; width: 776px; height: 732px; border-radius: 18px;
    background: linear-gradient(180deg, #a9c6e6 0%, #e6e8df 50%, #c9bf78 100%);
  }
  .meta { position: absolute; top: 1144px; left: 48px; list-style: none; }
  .meta li { display: flex; align-items: center; height: 112px; font-size: 42px; }
  .meta svg { width: 72px; height: 72px; margin-right: 44px; }
  .meta .temp { font-family: "Josefin Sans", sans-serif; font-weight: 600; font-size: 46px; }
  .meta .temp sup { font-size: 30px; font-weight: 400; }
  .diary-body {
    position: absolute; top: 1550px; left: 0; width: 780px;
    font-size: 43px; line-height: 76px; letter-spacing: 1px;
  }
  .tab-bar {
    position: absolute; left: 0; bottom: 0; width: 1200px; height: 204px;
    background: var(--nav-bg); box-shadow: 0 -6px 24px rgba(0,0,0,0.06);
    border-radius: 0 0 64px 64px;
  }
  .tab-bar svg { position: absolute; top: 60px; width: 84px; height: 84px; }
</style>
</head>
<body>
<main class="screen">
  <div class="binding" role="img" aria-label="ノートのリング綴じ"></div>

  <article class="page">
    <h1 class="diary-title">HOSHIZORA Note</h1>
    <p class="diary-date">2023<small>年</small>03<small>月</small>16<small>日</small><span class="weekday">（wed）</span></p>
    <div class="sunrise-photo" role="img" aria-label="朝日が昇る山と草原の写真"></div>

    <ul class="meta">
      <li>
        <svg viewBox="0 0 24 24" fill="none" stroke="var(--icon-green)" stroke-width="2" stroke-linecap="round"><circle cx="12" cy="12" r="4"/><path d="M12 2v3M12 19v3M2 12h3M19 12h3M4.9 4.9l2.1 2.1M17 17l2.1 2.1M4.9 19.1L7 17M17 7l2.1-2.1"/></svg>
        <span>快晴</span>
      </li>
      <li>
        <svg viewBox="0 0 24 24"><path d="M12 2a7 7 0 0 0-7 7c0 5 7 13 7 13s7-8 7-13a7 7 0 0 0-7-7z" fill="var(--icon-green)"/><circle cx="12" cy="9" r="2.6" fill="var(--paper)"/></svg>
        <span>東京都渋谷区</span>
      </li>
      <li>
        <svg viewBox="0 0 24 24" fill="none" stroke="var(--icon-green)" stroke-width="2" stroke-linecap="round"><path d="M10 4a2 2 0 0 1 4 0v10a4 4 0 1 1-4 0z"/><path d="M12 9v7"/></svg>
        <span class="temp">20.3<sup>°</sup>C</span>
      </li>
    </ul>

    <p class="diary-body">日記のテキストが入ります。日記のテキストが入ります。日記のテキストが入ります。日記のテキストが入ります。日記のテキストが入ります。日記のテキストが入ります。日記のテキストが入ります。日記のテキストが入ります。日記のテキストが入ります。日記のテキストが入ります。日記のテキストが入ります。</p>
  </article>

  <nav class="tab-bar" aria-label="メニュー">
    <svg style="left:138px" viewBox="0 0 24 24" fill="var(--nav-icon)"><path d="M12 3L2 12h3v8h5v-5h4v5h5v-8h3z"/></svg>
    <svg style="left:346px" viewBox="0 0 24 24" fill="none" stroke="var(--nav-icon)" stroke-width="2.2" stroke-linecap="round"><circle cx="10" cy="10" r="6.5"/><path d="M15 15l6 6"/></svg>
    <svg style="left:558px" viewBox="0 0 24 24" fill="none" stroke="var(--nav-icon)" stroke-width="2"><path d="M12 20s-8-5-8-11a4.5 4.5 0 0 1 8-2.8A4.5 4.5 0 0 1 20 9c0 6-8 11-8 11z"/></svg>
    <svg style="left:766px" viewBox="0 0 24 24" fill="var(--ink)"><rect x="3" y="3" width="4" height="4"/><rect x="10" y="3" width="4" height="4"/><rect x="17" y="3" width="4" height="4"/><rect x="3" y="10" width="4" height="4"/><rect x="10" y="10" width="4" height="4"/><rect x="17" y="10" width="4" height="4"/><rect x="3" y="17" width="4" height="4"/><rect x="10" y="17" width="4" height="4"/><rect x="17" y="17" width="4" height="4"/></svg>
    <svg style="left:970px" viewBox="0 0 24 24" fill="none" stroke="var(--nav-icon)" stroke-width="2"><circle cx="12" cy="8" r="4.5"/><path d="M4 21v-1a5 5 0 0 1 5-5h6a5 5 0 0 1 5 5v1z"/></svg>
  </nav>
</main>
</body>
</html>
```